Looking for a modern elegant home improvment website

Looking for a new Design on current website . Please us www.pinegablebuilders.com PIctures of recent work and stock photos that were attached , Free estimates , Explaining what we do , Similiar to www. pinegablebuilders.com which is our current webpage . Colors can be different . I have attached our buisness card as well as our postcard we send out to homes . I would like a modern web page that our costumers can feel is professional so they can have a feeling of trust when they hire us . Our address should be on there . Licenesed & Insured should be somewhere on the page . Our Company Logo should be there as well . It would be nice to have a very modern website with great pictures of home interiors and exteriors . a page describing what we do is very important . facebook link to our page is a must as well as a instagram .
Updates

Reason: Looking for a elegant modern 5 page website with proper spelling and professional looking . I extended the deadline and upgraded .

Reason: Looking for more design options .

Target Market(s)

Home owners , Commerical buisness,

Industry/Entity Type

Home Improvement

Number of Pages Required

5+ page

Font styles to use
Serif

Requirements
Must have
• PIctures of recent work and stock photos that were attached , Free estimates , Explaining what we do , Similiar to www. pinegablebuilders.com which is our current webpage . Colors can be different . I have attached our buisness card as well as our postcard we send out to homes . I would like a modern web page that our costumers can feel is professional so they can have a feeling of trust when they hire us . Our address should be on there . Licenesed & Insured should be somewhere on the page . Our Company Logo should be there as well .
Nice to have
• It would be nice to have a very modern website with great pictures of home interiors and exteriors . a page describing what we do is very important . facebook link to our page is a must as well as a instagram .

```html
<!DOCTYPE html>
<html lang="en">
<head>
<meta charset="utf-8">
<title>Pine Gable Builders LLC</title>
<link href="https://fonts.googleapis.com/css2?family=Roboto:wght@300;400;500;700;900&display=swap" rel="stylesheet">
<style>
:root{
  --navy:#3b4d80;
  --navy-deep:#2e3f70;
  --sage:#65997b;
  --forest:#2b4c3d;
  --paper:#ececec;
  --ink:#2a2a2a;
  --white:#ffffff;
  --mint:#7fc79f;
}
*{margin:0;padding:0;box-sizing:border-box}
html,body{width:1179px;height:1200px;overflow:hidden}
body{position:relative;font-family:'Roboto',sans-serif;background:var(--white);color:var(--ink)}
.abs{position:absolute}

/* header */
.brand{left:0;top:0;width:344px;height:149px;background:var(--white);display:flex;align-items:center;justify-content:center;gap:8px}
.brand-mark{width:14px;height:14px;background:var(--forest)}
.brand-name{font-size:17px;font-weight:500;color:var(--forest);letter-spacing:.5px}

.contacts{left:344px;top:0;width:835px;height:149px;background:var(--navy);color:var(--white)}
.contacts-title{left:40px;top:14px;font-size:19px;letter-spacing:1px}
.contacts-rule{left:0;top:45px;width:835px;height:1px;background:rgba(255,255,255,.25)}
.follow{top:15px;width:100px;height:20px;background:#eef1f6;border:1px solid #c9d0dd;border-radius:2px;display:flex;align-items:center;justify-content:space-between;padding:0 3px 0 6px;font-size:10px;font-weight:500;color:var(--navy)}
.follow span.sq{width:16px;height:16px;background:var(--navy)}
.phone-box{left:33px;top:71px;width:52px;height:47px;background:var(--navy-deep);border:1px solid #26356a;display:flex;align-items:center;justify-content:center}
.person{top:70px;font-size:14px;letter-spacing:.3px}
.person .tel{font-size:17px;margin-top:3px;letter-spacing:.5px}
.person .mail{font-size:9.5px;margin-top:6px}

/* nav */
.nav{left:0;top:149px;width:1179px;height:50px;background:var(--sage)}
.nav-active{left:208px;top:0;width:137px;height:50px;background:var(--forest)}
.nav-item{top:14px;font-size:17px;color:var(--white);letter-spacing:.3px}

/* hero */
.hero{left:0;top:199px;width:1179px;height:609px;background:linear-gradient(180deg,#d6d0c6 0%,#b9b1a4 42%,#8a5e3e 62%,#6b4428 100%)}
.hero-shade{left:0;top:0;width:490px;height:609px;background:rgba(40,40,40,.45)}
.hero-panel{left:85px;top:192px;width:664px;height:159px;background:var(--sage);color:var(--white);padding:16px 0 0 23px}
.hero-title{font-size:63px;font-weight:700;letter-spacing:5px;line-height:1}
.hero-sub{font-size:45px;font-weight:300;letter-spacing:1px;margin-top:6px;line-height:1.05}
.hero-btn{left:85px;top:367px;width:148px;height:46px;background:var(--white);color:var(--navy);font-size:18px;display:flex;align-items:center;justify-content:center;letter-spacing:.3px}
.dots{left:947px;top:564px;width:148px;height:6px;display:flex}
.dots i{flex:1;background:var(--white)}
.dots i.on{background:var(--sage)}

/* welcome */
.welcome{left:0;top:808px;width:589px;height:392px;background:var(--paper)}
.welcome h1{position:absolute;left:86px;top:37px;font-size:41px;font-weight:300;color:#222}
.rule{height:1px}
.welcome .rule{position:absolute;left:85px;top:91px;width:492px;background:#b8b8b8}
.welcome p{position:absolute;left:86px;top:112px;width:490px;font-size:12.2px;line-height:19px;color:#333}
.welcome-btn{left:85px;top:264px;width:148px;height:34px;background:var(--navy);color:var(--white);font-size:13.5px;font-weight:500;display:flex;align-items:center;justify-content:center}
.tools{left:298px;top:254px;width:280px;height:120px;border-radius:40px;background:radial-gradient(ellipse at 35% 45%,#f3cf3a 0%,#c89a55 45%,rgba(150,120,90,.25) 75%,rgba(236,236,236,0) 100%)}

/* what we do */
.services{left:589px;top:808px;width:590px;height:392px;background:var(--navy);color:var(--white)}
.services h2{position:absolute;left:32px;top:50px;font-size:26px;font-weight:300;letter-spacing:.5px}
.services .rule{position:absolute;left:32px;top:91px;width:491px;background:rgba(255,255,255,.3)}
.services p{position:absolute;left:32px;top:114px;width:500px;font-size:12.2px;line-height:19px}
.svc{font-size:12.2px;display:flex;align-items:center;gap:11px;letter-spacing:.2px}
.more{left:278px;top:296px;font-size:13px;font-weight:500;color:var(--mint);letter-spacing:.5px}
</style>
</head>
<body>

<header>
  <div class="abs brand">
    <span class="brand-mark"></span>
    <span class="brand-name">Pine Gable Builders LLC</span>
  </div>

  <div class="abs contacts">
    <div class="abs contacts-title">Contacts:</div>
    <div class="abs follow" style="left:542px">Follow us on<span class="sq"></span></div>
    <div class="abs follow" style="left:652px">Follow us on<span class="sq"></span></div>
    <div class="abs contacts-rule"></div>

    <div class="abs phone-box">
      <svg width="22" height="22" viewBox="0 0 24 24" aria-hidden="true"><path fill="#8ea0d6" d="M6.6 10.8a15.1 15.1 0 0 0 6.6 6.6l2.2-2.2c.3-.3.7-.4 1-.2 1.1.4 2.3.6 3.6.6.6 0 1 .4 1 1V20c0 .6-.4 1-1 1A17 17 0 0 1 3 4c0-.6.4-1 1-1h3.5c.6 0 1 .4 1 1 0 1.3.2 2.5.6 3.6.1.3 0 .7-.2 1z"/></svg>
    </div>

    <div class="abs person" style="left:96px">Marco Delgado<div class="tel">555-210-4410</div><div class="mail" style="margin-top:4px">pinegablebuilders@mail.com</div></div>
    <div class="abs person" style="left:258px">Tomas Delgado<div class="tel">555-318-2276</div><div class="mail">pinegablebuilders@mail.com</div></div>
    <div class="abs person" style="left:432px">Portuguese or Spanish, Rui Delgado<div class="tel">555-210-4482</div><div class="mail">pinegablebuilders@mail.com</div></div>
  </div>

  <nav class="abs nav">
    <div class="abs nav-active"></div>
    <span class="abs nav-item" style="left:255px">Home</span>
    <span class="abs nav-item" style="left:372px">About Us</span>
    <span class="abs nav-item" style="left:515px">Services</span>
    <span class="abs nav-item" style="left:653px">Gallery</span>
    <span class="abs nav-item" style="left:778px">Contact Us</span>
  </nav>
</header>

<section class="abs hero" role="img" aria-label="Photo of a finished basement with drop ceiling, recessed lights, white door and wide-plank wood floor">
  <div class="abs hero-shade"></div>
  <div class="abs hero-panel">
    <div class="hero-title">Free Estimates</div>
    <div class="hero-sub">Licensed &amp; Fully Insured</div>
  </div>
  <div class="abs hero-btn">Read More</div>
  <div class="abs dots"><i></i><i class="on"></i><i></i></div>
</section>

<section class="abs welcome">
  <h1>Welcome to!</h1>
  <div class="rule"></div>
  <p>Your home is the most important asset you have, so when you’re ready to build or remodel, get yourself the best General Contractor in the business!<br>We have been building for over 20 years, specializing in residential construction. We are tile &amp; marble specialist. We build bathrooms, Kitchens, Additions and much more. Give us a try, we do great work and are very passionate about what we do. We are a family owned business that has been in the construction field for<br>over 20 years.</p>
  <div class="abs welcome-btn">READ MORE</div>
  <div class="abs tools" role="img" aria-label="Illustration of a yellow hard hat, tool belt, level and hammer"></div>
</section>

<section class="abs services">
  <h2>What We Do</h2>
  <div class="rule"></div>
  <p>Nulla quis molestie mauris. Etiam eu luctus arcu. Vivamus scelerisque augue nibh,Nulla quis molestie mauris. Etiam eu luctus arcu. Vivamus scelerisque augue nibh, Pellentesque pulvinar viverra sollicitudin.</p>

  <svg width="0" height="0" style="position:absolute"><defs><symbol id="bullet" viewBox="0 0 12 12"><circle cx="6" cy="6" r="6" fill="#7fc79f"/><path d="M5 3.5 7.5 6 5 8.5" stroke="#3b4d80" stroke-width="1.6" fill="none"/></symbol></defs></svg>

  <div class="abs svc" style="left:34px;top:196px"><svg width="12" height="12"><use href="#bullet"/></svg>Nulla quis molestie mauris.</div>
  <div class="abs svc" style="left:34px;top:227px"><svg width="12" height="12"><use href="#bullet"/></svg>Etiam eu luctus arcu vivamus</div>
  <div class="abs svc" style="left:34px;top:258px"><svg width="12" height="12"><use href="#bullet"/></svg>Scelerisque augue nibh,</div>
  <div class="abs svc" style="left:34px;top:289px"><svg width="12" height="12"><use href="#bullet"/></svg>Nulla quis molestie mauris.</div>

  <div class="abs svc" style="left:277px;top:196px"><svg width="12" height="12"><use href="#bullet"/></svg>Nulla quis molestie mauris.</div>
  <div class="abs svc" style="left:277px;top:227px"><svg width="12" height="12"><use href="#bullet"/></svg>Etiam eu luctus arcu vivamus</div>
  <div class="abs svc" style="left:277px;top:258px"><svg width="12" height="12"><use href="#bullet"/></svg>Scelerisque augue nibh,</div>
  <div class="abs more">MORE...</div>
</section>

</body>
</html>
```